Business Card Design Project

Name of Company: Halvorine Coaching & Consulting
Possible Acronym: HC&C
My Name: Mirabel Halvorine, LL.B.
My email address: mirabel@halvorineconsulting.example
My tel.: +44 (0) 7938 604 275
My skype address: halvorinehc
I am offering executive coaching and consulting in the area of business development and strategic planning to intellectual property law firms around the world.
Since I will be marketing to the legal industry, the card must be fairly conservative. However I want it to also have flare and spark. I want to convey to potential clients that I can be the spark that will ignite their potential. I like the combination of navy blue and hot pink. However, I have decided that hot pink is not corporate enough so I would like to use a colour with navy that comes close to hot pink but is more conservative. Not red. I would consider swapping navy blue for grey if you thought that would look better. I would like the background of the card to be entirely white - both back and front - only the letters will be in colour.
I would like the card to be double sided with the name of my firm (or the acronym) and my email address underneath (mirabel@halvorineconsulting.example) on the back and on the front, all of the information above.
With gratitude!
Mirabel

```html
<!DOCTYPE html>
<html lang="en">
<head>
<meta charset="utf-8">
<title>Halvorine Coaching &amp; Consulting — Business Card</title>
<link rel="stylesheet" href="https://fonts.googleapis.com/css2?family=Marcellus+SC&family=Didact+Gothic&display=swap">
<style>
  :root {
    --page: #e6e7ea;
    --card: #ffffff;
    --navy: #1c2a5c;
    --grey-text: #8e8f93;
    --grey-soft: #d9dadd;
    --grey-softer: #eeeff1;
    --rule: #b9babd;
    --shadow: rgba(20, 24, 40, 0.18);
  }
  * { margin: 0; padding: 0; box-sizing: border-box; }
  html, body {
    width: 1200px;
    height: 984px;
    overflow: hidden;
    background: var(--page);
  }
  .sheet {
    width: 1200px;
    height: 984px;
    display: flex;
    flex-direction: column;
    align-items: center;
    justify-content: center;
    gap: 40px;
  }
  .card {
    position: relative;
    width: 760px;
    height: 434px;
    background: var(--card);
    box-shadow: 0 6px 18px var(--shadow);
  }

  /* ---------- Back side ---------- */
  .back__flourish {
    position: absolute;
    left: 90px;
    top: 24px;
    width: 580px;
    height: 180px;
  }
  .back__band {
    position: absolute;
    left: 40px; right: 40px;
    top: 232px;
    border-top: 1px solid var(--rule);
    border-bottom: 1px solid var(--rule);
    padding: 8px 0 6px;
    text-align: center;
    font-family: "Marcellus SC", serif;
    font-size: 30px;
    letter-spacing: 1.5px;
    color: var(--navy);
  }
  .back__web {
    position: absolute;
    right: 48px;
    top: 300px;
    font-family: "Didact Gothic", sans-serif;
    font-size: 18px;
    letter-spacing: 1.5px;
    color: var(--grey-text);
  }

  /* ---------- Front side ---------- */
  .front__band {
    position: absolute;
    left: 40px; right: 40px;
    top: 48px;
    border-top: 1px solid var(--rule);
    border-bottom: 1px solid var(--rule);
    padding: 7px 0 5px;
    text-align: center;
    font-family: "Marcellus SC", serif;
    font-size: 27px;
    letter-spacing: 1.2px;
    color: var(--navy);
  }
  .front__tagline {
    position: absolute;
    left: 0; right: 0;
    top: 104px;
    text-align: center;
    font-family: "Didact Gothic", sans-serif;
    font-size: 19px;
    letter-spacing: 3px;
    color: var(--grey-text);
  }
  .front__name {
    position: absolute;
    left: 0; right: 0;
    top: 160px;
    text-align: center;
    font-family: "Marcellus SC", serif;
    font-size: 44px;
    letter-spacing: 1.5px;
    color: var(--navy);
  }
  .front__contacts {
    position: absolute;
    left: 56px;
    top: 258px;
    display: grid;
    grid-template-columns: auto auto;
    column-gap: 22px;
    row-gap: 6px;
    font-family: "Didact Gothic", sans-serif;
    font-size: 19px;
    letter-spacing: 1.5px;
  }
  .contact__label { color: var(--navy); text-align: right; }
  .contact__value { color: var(--grey-text); }
</style>
</head>
<body>
<main class="sheet">
  <section class="card card--back" aria-label="Card back">
    <svg class="back__flourish" viewBox="0 0 580 180" role="img" aria-label="Large decorative hand-lettered first name in light grey">
      <defs>
        <linearGradient id="flourishTone" x1="0" y1="0" x2="1" y2="1">
          <stop offset="0" stop-color="var(--grey-softer)"/>
          <stop offset="1" stop-color="var(--grey-soft)"/>
        </linearGradient>
      </defs>
      <rect width="580" height="180" rx="6" fill="url(#flourishTone)"/>
    </svg>
    <div class="back__band">Halvorine Coaching &amp; Consulting</div>
    <div class="back__web">halvorineconsulting.example</div>
  </section>

  <section class="card card--front" aria-label="Card front">
    <div class="front__band">Halvorine Coaching &amp; Consulting</div>
    <div class="front__tagline">sparking the potential in you</div>
    <div class="front__name">Mirabel Halvorine, LL.B.</div>
    <dl class="front__contacts">
      <dt class="contact__label">e-mail</dt>
      <dd class="contact__value">mirabel@halvorineconsulting.example</dd>
      <dt class="contact__label">phone</dt>
      <dd class="contact__value">+44 (0) 7938 604 275</dd>
      <dt class="contact__label">skype</dt>
      <dd class="contact__value">halvorinehc</dd>
    </dl>
  </section>
</main>
</body>
</html>
```